Postcard Design for Brindlewood Pine Acres LLC

We are a small family owned Christmas tree farm. We work with various groups on their fundraising programs selling wreaths and trees. Our goal is to expand our business, advertising with post cards.

Target Market(s)

Schools, Trail Rangers, various non profit groups

Industry/Entity Type

Advertising

Requirements
Must have
• Front side-

Let us help you develop a successful holiday fundraiser for your group with fresh, fragrant Wisconsin wreaths shipped directly from our farm!

Picture of a real wreath with a red bow and 2 pinecone clusters at 4 o'clock and 8 o'clock.

Contact information -
Brindlewood Pine Acres LLC
www.brindlewoodpineacres.com
555-147-9362

Backside -
We have 2 different type of wreath fundraising programs - mail order and direct distribution. You group can choose to do one or both. Wholesale Christmas trees are also available.

```html
<!DOCTYPE html>
<html lang="en">
<head>
<meta charset="utf-8">
<title>Brindlewood Pine Acres – Fundraising Postcard</title>
<link rel="stylesheet" href="https://fonts.googleapis.com/css2?family=Arimo:wght@400;700&family=Tinos:wght@400;700&display=swap">
<style>
  :root {
    --forest: #1f7a3a;
    --brand-green: #1c8a3e;
    --sun-yellow: #f7e83a;
    --white: #ffffff;
    --tan: #c9b99a;
    --ink: #2a2a2a;
    --tick-red: #d4141c;
    --zone-pink: #f6c1c7;
    --card-border: #9a9a9a;
    --band-grey: #d9dcd6;
    --page: #ffffff;
  }
  * { margin: 0; padding: 0; box-sizing: border-box; }
  html, body { width: 1200px; height: 656px; overflow: hidden; background: var(--page); }
  .canvas { position: relative; width: 1200px; height: 656px; font-family: "Tinos", "Times New Roman", serif; }

  /* Front side */
  .front { position: absolute; left: 39px; top: 41px; width: 444px; height: 570px; overflow: hidden; background: var(--forest); }
  .front-art { position: absolute; left: 0; top: 0; width: 444px; height: 300px; }
  .front-brand { position: absolute; left: 322px; top: 12px; color: var(--white); font-size: 20px; line-height: 29px; }
  .front-headline { position: absolute; left: 16px; top: 296px; color: var(--sun-yellow); font-weight: 700; font-size: 22px; line-height: 31px; }
  .front-headline .lead { padding-left: 6px; }
  .benefits { position: absolute; left: 70px; top: 391px; list-style: none; color: var(--white); font-weight: 700; font-size: 14px; line-height: 19.5px; white-space: nowrap; }
  .benefits li { display: flex; align-items: center; gap: 8px; }
  .benefits svg { width: 16px; height: 15px; flex: none; }
  .front-footer { position: absolute; left: 0; top: 478px; width: 100%; height: 92px; background: var(--tan); color: var(--ink); text-align: center; font-weight: 700; }
  .front-footer .url { font-size: 25px; line-height: 32px; padding-top: 16px; }
  .front-footer .phone { font-size: 25px; line-height: 32px; }

  /* Back side */
  .back { position: absolute; left: 568px; top: 102px; width: 573px; height: 436px; background: var(--white); border: 1px solid var(--card-border); overflow: hidden; }
  .zone { position: absolute; background: var(--zone-pink); font-family: "Arimo", Arial, sans-serif; color: var(--ink); }
  .zone-postage { left: 442px; top: 0; width: 131px; height: 140px; text-align: center; font-size: 14px; line-height: 17px; padding-top: 55px; }
  .zone-address { left: 284px; top: 139px; width: 289px; height: 231px; }
  .zone-address .label { position: absolute; left: 0; width: 100%; top: 35px; text-align: center; font-size: 15px; line-height: 18px; }
  .zone-address .rule { position: absolute; left: 31px; top: 84px; width: 240px; font-size: 11px; line-height: 13.5px; }
  .zone-barcode { left: 72px; top: 369px; width: 501px; height: 67px; text-align: center; font-size: 15px; line-height: 67px; }
  .farm-photo { position: absolute; left: 53px; top: 52px; width: 160px; height: 160px; transform: rotate(7deg); background: linear-gradient(170deg, #9fbfa0 0%, #4d8a4f 35%, #2f6e38 70%, #6aa05e 100%); box-shadow: 0 1px 3px rgba(0,0,0,.25); }
  .back-brand { position: absolute; left: 305px; top: 40px; color: var(--brand-green); font-size: 23px; line-height: 33px; }
  .back-offer { position: absolute; left: 10px; top: 241px; width: 274px; text-align: center; color: var(--brand-green); font-size: 21px; line-height: 30px; }
  .back-contact { position: absolute; left: 10px; top: 306px; width: 274px; text-align: center; color: var(--ink); font-weight: 700; }
  .back-contact .url { font-size: 15.5px; line-height: 20px; }
  .back-contact .phone { font-size: 25px; line-height: 34px; }
</style>
</head>
<body>
<div class="canvas">

  <section class="front">
    <svg class="front-art" viewBox="0 0 444 300">
      <defs>
        <linearGradient id="doorTones" x1="0" y1="0" x2="1" y2="1">
          <stop offset="0" stop-color="#5a2a18"/>
          <stop offset="0.45" stop-color="#7a3d22"/>
          <stop offset="0.55" stop-color="#4f6a3a"/>
          <stop offset="1" stop-color="#3d1c10"/>
        </linearGradient>
      </defs>
      <rect width="444" height="300" fill="var(--forest)"/>
      <path d="M0,60 Q200,20 444,80 L444,94 Q200,38 0,76 Z" fill="var(--band-grey)"/>
      <path d="M0,76 Q200,38 444,94 L444,262 Q260,238 0,286 Z" fill="url(#doorTones)" role="img" aria-label="Photo of a wooden front door with a fresh evergreen wreath, red bow and pinecone clusters"/>
      <path d="M0,286 Q260,238 444,262 L444,276 Q260,256 0,300 Z" fill="var(--band-grey)"/>
    </svg>
    <div class="front-brand">Brindlewood<br>Pine Acres</div>
    <h1 class="front-headline"><span class="lead">Let Brindlewood</span><br>Pine Acres Help With<br>Your Fundraising Needs!</h1>
    <ul class="benefits">
      <li><svg viewBox="0 0 16 15"><path d="M1,8 L6,13 L15,1" fill="none" stroke="var(--tick-red)" stroke-width="3" stroke-linecap="round" stroke-linejoin="round"/></svg>Proven track record of success.</li>
      <li><svg viewBox="0 0 16 15"><path d="M1,8 L6,13 L15,1" fill="none" stroke="var(--tick-red)" stroke-width="3" stroke-linecap="round" stroke-linejoin="round"/></svg>Fresh, fragrant premium quality wreaths.</li>
      <li><svg viewBox="0 0 16 15"><path d="M1,8 L6,13 L15,1" fill="none" stroke="var(--tick-red)" stroke-width="3" stroke-linecap="round" stroke-linejoin="round"/></svg>Shipped directly from our Wisconsin farm.</li>
      <li><svg viewBox="0 0 16 15"><path d="M1,8 L6,13 L15,1" fill="none" stroke="var(--tick-red)" stroke-width="3" stroke-linecap="round" stroke-linejoin="round"/></svg>Mail Order or Direct Distribution (or both).</li>
    </ul>
    <footer class="front-footer">
      <div class="url">www.brindlewoodpineacres.com</div>
      <div class="phone">555-147-9362</div>
    </footer>
  </section>

  <section class="back">
    <div class="zone zone-postage">Postage<br>Area</div>
    <div class="zone zone-address">
      <div class="label">Address Area</div>
      <p class="rule">The only text allowed in the Address Area<br>is the recipient mailing address.<br>Red zones may have no text or<br>graphics darker than 7% grayscale.</p>
    </div>
    <div class="zone zone-barcode">Barcode Area</div>
    <div class="farm-photo" role="img" aria-label="Photo of rows of young Christmas trees growing on the farm"></div>
    <div class="back-brand">Brindlewood<br>Pine Acres</div>
    <p class="back-offer">Wholesale Trees<br>Also Available</p>
    <div class="back-contact">
      <div class="url">www.brindlewoodpineacres.com</div>
      <div class="phone">555-147-9362</div>
    </div>
  </section>

</div>
</body>
</html>
```